PlumEcho Social Sharing Platform Needs a Redesign (2 pages / Design only)

PlumEcho is a popular social sharing platform for bloggers and marketers. The site has been quite popular for a few years now, but the site's design is looking quite dated. We're looking for a brand new design to give the service a facelift.

We are looking for a modern and fresh design that keeps all the existing functionality intact. Would prefer designs that incorporate the color blue in them.

We would like the two attached screenshots to be redesigned and submitted - using he same content. Please do not submit a redesign of the front page (non-logged in version). Redesign the 2 attached pages only, and the final deliverable is these two pages as layered PSD files.

Target Market(s)

bloggers, internet marketers

Industry/Entity Type

Social

Number of Pages Required

2 page

Requirements
Must have
• All existing functionality must be intact as seen from the screenshots.
Should not have
• Please do not submit designs based on existing front page (non-logged in version). Use attached screenshots (file 1 and 2) as a guide of existing functionality.

```html
<!DOCTYPE html>
<html lang="en">
<head>
<meta charset="utf-8">
<title>PlumEcho – Timeline</title>
<link href="https://fonts.googleapis.com/css2?family=PT+Sans:wght@400;700&family=Titillium+Web:wght@600;700&family=Arimo:wght@400;700&display=swap" rel="stylesheet">
<style>
:root{
  --blue:#0f65b0;
  --panel-blue:#1a84c7;
  --heading-blue:#1479c4;
  --orange:#f07f0a;
  --coral:#f26b3a;
  --dark:#3a3a3a;
  --grey-bg:#f1f1f1;
  --text:#222;
  --muted:#9a9a9a;
  --link-blue:#2a5aa0;
  --black:#000;
}
*{box-sizing:border-box;margin:0;padding:0}
html,body{width:934px;height:1200px;overflow:hidden;background:#fff}
body{font-family:"Arimo",Arial,sans-serif;color:var(--text)}
.page{position:relative;width:934px;height:1200px;overflow:hidden}
.abs{position:absolute}

.logo{left:80px;top:22px;display:flex;align-items:center;gap:7px;color:var(--blue);font-family:"PT Sans",sans-serif;font-weight:700;font-size:27px;letter-spacing:.5px}
.logo .dot{width:14px;height:14px;border-radius:50%;background:currentColor}
.toplinks{right:77px;top:36px;font-family:"PT Sans",sans-serif;font-weight:700;font-size:12px;color:#333}
.toplinks span{margin:0 7px}
.toplinks .sep{margin:0}

.mainnav{left:0;top:71px;width:934px;height:32px;background:var(--blue);display:flex;align-items:center;padding-left:84px}
.mainnav a{color:#fff;text-decoration:none;font-family:"PT Sans",sans-serif;font-size:13px;margin-right:38px}

.hero-band{left:0;top:103px;width:934px;height:257px;background:var(--grey-bg)}
.cover{left:82px;top:112px;width:517px;height:175px;background:linear-gradient(100deg,#e8ecee 0%,#cfd8de 35%,#e9d5c4 60%,#f0ede9 100%)}
.profile-bar{left:84px;top:287px;width:514px;height:40px;background:#fff;border:1px solid #e6e6e6;border-top:none}
.avatar{left:105px;top:248px;width:76px;height:76px;border-radius:50%;background:radial-gradient(circle at 50% 40%,#c89a7c,#7a5a48);border:3px solid #fff;box-shadow:0 0 0 1px #ddd}
.profile-name{left:190px;top:256px;font-size:20px;color:#222}
.tabs{left:188px;top:288px;height:38px;display:flex;font-size:10px}
.tabs .tab{display:flex;align-items:center;gap:5px;padding:0 12px;border-right:1px solid #ececec;color:#b5b5b5}
.tabs .tab.active{color:#444}

.search-panel{left:617px;top:113px;width:241px;height:203px;background:var(--panel-blue);border-radius:2px}
.field{position:absolute;left:16px;background:#fff;height:26px;font-size:10px;color:#333;padding:0 7px;display:flex;align-items:center;justify-content:space-between}
.btn-search{position:absolute;left:17px;top:151px;width:63px;height:22px;background:var(--orange);border-radius:3px;color:#fff;font-size:12px;display:flex;align-items:center;justify-content:center}

.post{left:77px;width:480px;height:90px}
.thumb{position:absolute;left:0;top:0;width:118px;height:86px;border:1px solid #c9c9c9;padding:4px;background:#f4f4f4}
.thumb div{width:100%;height:100%}
.post .author{position:absolute;left:125px;top:3px;color:var(--link-blue);font-weight:700;font-size:11px}
.post .meta{position:absolute;left:127px;top:24px;display:flex;align-items:center;font-size:11px;color:#333}
.stars{display:flex;gap:1px;margin-right:12px}
.stars i{width:11px;height:11px;background:#f39a1a;display:block;position:relative}
.stars i.off{background:#ddd}
.stars i::after{content:"★";position:absolute;inset:0;color:#fff;font-style:normal;font-size:9px;line-height:11px;text-align:center}
.meta .act{display:flex;align-items:center;gap:7px;margin-right:22px}
.post p{position:absolute;left:127px;top:44px;width:360px;font-size:10.5px;line-height:12.6px;color:#222}
.divider{left:77px;width:480px;height:1px;background:#d8d8d8}

.bday-head{left:611px;top:380px;width:248px;height:55px;background:var(--dark);border-bottom:3px solid var(--coral);color:#fff;display:flex;align-items:center;padding-left:20px;gap:9px}
.bday-head h3{font-family:"PT Sans",sans-serif;font-size:16px;font-weight:700;line-height:16px}
.bday-head small{display:block;font-size:10px;color:#c8c8c8;font-weight:700;letter-spacing:.3px}
.bday-item{left:632px;width:206px;height:62px}
.bday-item .pic{position:absolute;left:0;top:0;width:60px;height:60px;border-radius:50%;background:radial-gradient(circle at 50% 40%,#c79a78,#4b3a30);border:3px solid #eee;box-shadow:0 0 0 1px #d7d7d7}
.bday-item .nm{position:absolute;left:74px;top:17px;color:var(--coral);font-family:"PT Sans",sans-serif;font-weight:700;font-size:14px}
.bday-item .yr{position:absolute;left:74px;top:35px;color:#aaa;font-size:10px;font-weight:700}
.dotted{left:627px;width:212px;border-top:1px dotted #cfcfcf}
.view-all{left:628px;top:702px;font-size:10px;font-weight:700;color:#9b9b9b}
.rule{left:611px;width:248px;height:2px;background:#e4e4e4}

.featured-bar{left:77px;top:777px;width:486px;height:32px;background:var(--heading-blue);border-radius:2px;color:#fff;font-family:"Titillium Web",sans-serif;font-weight:600;font-size:20px;padding-left:14px;line-height:32px;letter-spacing:.3px}
.featured-img{left:78px;top:828px;width:484px;height:134px;background:linear-gradient(135deg,#7d7d7d 0%,#5a5a5a 35%,#2f7bb8 55%,#9a9a9a 80%,#6f6f6f 100%)}
.featured-title{left:91px;top:834px;color:#fff;font-family:"Titillium Web",sans-serif;font-weight:700;font-size:23px;letter-spacing:1px}
.featured-text{left:78px;top:971px;width:486px;font-size:11.5px;line-height:17px;color:#222}

.seo-title{left:611px;top:773px;color:var(--heading-blue);font-family:"Titillium Web",sans-serif;font-weight:700;font-size:20px;line-height:22px;letter-spacing:.3px}
.chart{left:612px;top:830px;width:244px;height:181px;border:1px solid #bbb;background:linear-gradient(90deg,#f6e2cc 0%,#dde6f6 35%,#efdcf0 55%,#f7ddd6 75%,#f2ead2 100%)}

.footer{left:0;top:1074px;width:934px;height:100px;background:var(--black)}
.copy{left:0;top:1174px;width:934px;height:26px;background:var(--blue);color:#fff;font-size:11px;text-align:center;line-height:26px}
.get-connected{left:85px;top:1102px;color:#ddd;font-family:"PT Sans",sans-serif;font-size:12px}
.social{left:80px;top:1126px;display:flex;gap:7px}
.social span{width:29px;height:29px;border-radius:50%;display:block}
.vline{top:1094px;height:80px;border-left:1px dotted #444}
.foot-links{left:256px;top:1108px;width:400px;text-align:center;font-family:"PT Sans",sans-serif;font-size:11.5px;color:#fff;line-height:23px}
.foot-links span{margin:0 12px}
.foot-logo{left:695px;top:1108px;display:flex;align-items:center;gap:7px;color:#fff;font-family:"PT Sans",sans-serif;font-weight:700;font-size:25px;letter-spacing:.5px}
.foot-logo .dot{width:13px;height:13px;border-radius:50%;background:#fff}
</style>
</head>
<body>
<div class="page">

  <header>
    <div class="abs logo"><span class="dot"></span>PlumEcho</div>
    <nav class="abs toplinks"><span>My Timeline</span><span class="sep">|</span><span>Edit Profile</span><span class="sep">|</span><span>Manage Friends</span><span class="sep">|</span><span>Messages</span></nav>
    <nav class="abs mainnav">
      <a>Dashboard</a><a>Chirpline Followers</a><a>Submit Chirp</a><a>Activity Summary</a><a>Buy Credits</a><a>Settings</a><a>Affiliates</a>
    </nav>
  </header>

  <section class="profile">
    <div class="abs hero-band"></div>
    <div class="abs cover" role="img" aria-label="Cover photo: smiling woman in a bright office"></div>
    <div class="abs profile-bar"></div>
    <div class="abs avatar" role="img" aria-label="Profile photo of Ben Darrow"></div>
    <div class="abs profile-name">Ben Darrow</div>
    <div class="abs tabs">
      <div class="tab active"><svg width="12" height="12" viewBox="0 0 12 12"><circle cx="6" cy="6" r="4" fill="none" stroke="#555" stroke-width="1.5"/><circle cx="6" cy="6" r="1.5" fill="#555"/></svg>Timeline</div>
      <div class="tab"><svg width="12" height="12" viewBox="0 0 12 12"><circle cx="6" cy="6" r="5" fill="none" stroke="#ccc"/><circle cx="6" cy="5" r="2" fill="#ccc"/></svg>About</div>
      <div class="tab"><svg width="16" height="12" viewBox="0 0 16 12"><circle cx="5" cy="4" r="2.5" fill="#ccc"/><circle cx="11" cy="4" r="2.5" fill="#ccc"/><rect x="1" y="7" width="14" height="5" rx="2" fill="#ccc"/></svg>Friends</div>
    </div>

    <form class="abs search-panel">
      <div class="field" style="top:17px;width:181px">Order by :<svg width="6" height="10" viewBox="0 0 6 10"><path d="M0 4 3 0 6 4ZM0 6 3 10 6 6Z" fill="#333"/></svg></div>
      <div class="field" style="top:62px;width:181px">All categories:<svg width="6" height="10" viewBox="0 0 6 10"><path d="M0 4 3 0 6 4ZM0 6 3 10 6 6Z" fill="#333"/></svg></div>
      <div class="field" style="top:106px;width:212px">Search (Keyword or Chirpline handle)</div>
      <div class="btn-search">SEARCH</div>
    </form>
  </section>

  <section class="feed">
    <article class="abs post" style="top:388px">
      <div class="thumb"><div role="img" aria-label="Programming book cover" style="background:linear-gradient(#3b3486 0 12%,#f5f5f0 12%)"></div></div>
      <div class="author">Mr. Alan Preston</div>
      <div class="meta"><div class="stars"><i></i><i></i><i></i><i></i><i class="off"></i></div>
        <span class="act"><svg width="15" height="13" viewBox="0 0 15 13"><path d="M1 1h13v8H6l-4 4V9H1z" fill="#1f5fae"/></svg>Comment</span>
        <span class="act"><svg width="18" height="12" viewBox="0 0 18 12"><rect width="18" height="12" fill="#1e4fd8"/><path d="M0 0 9 7 18 0" fill="none" stroke="#fff"/></svg>Email</span></div>
      <p>Your chance to ask questions, get answer, simply dummy text of the printing and typesetting industry. Lorem Ipsum has been the industry's standard dummy text ever since</p>
    </article>
    <div class="abs divider" style="top:491px"></div>

    <article class="abs post" style="top:509px">
      <div class="thumb"><div role="img" aria-label="Group of friends sharing snacks" style="background:linear-gradient(90deg,#b9c6cc,#d8b39a,#c9a98a)"></div></div>
      <div class="author">Mr. Alan Preston</div>
      <div class="meta"><div class="stars"><i></i><i></i><i></i><i></i><i class="off"></i></div>
        <span class="act"><svg width="15" height="13" viewBox="0 0 15 13"><path d="M1 1h13v8H6l-4 4V9H1z" fill="#1f5fae"/></svg>Comment</span>
        <span class="act"><svg width="18" height="12" viewBox="0 0 18 12"><rect width="18" height="12" fill="#1e4fd8"/><path d="M0 0 9 7 18 0" fill="none" stroke="#fff"/></svg>Email</span></div>
      <p>Your chance to ask questions, get answer, simply dummy text of the printing and typesetting industry. Lorem Ipsum has been the industry's standard dummy text ever since</p>
    </article>
    <div class="abs divider" style="top:611px"></div>

    <article class="abs post" style="top:626px">
      <div class="thumb"><div role="img" aria-label="Film cast group scene" style="background:linear-gradient(160deg,#7a7f8a,#3a3030 60%,#2a2020)"></div></div>
      <div class="author">Mr. Alan Preston</div>
      <div class="meta"><div class="stars"><i></i><i></i><i></i><i></i><i class="off"></i></div>
        <span class="act"><svg width="15" height="13" viewBox="0 0 15 13"><path d="M1 1h13v8H6l-4 4V9H1z" fill="#1f5fae"/></svg>Comment</span>
        <span class="act"><svg width="18" height="12" viewBox="0 0 18 12"><rect width="18" height="12" fill="#1e4fd8"/><path d="M0 0 9 7 18 0" fill="none" stroke="#fff"/></svg>Email</span></div>
      <p>Your chance to ask questions, get answer, simply dummy text of the printing and typesetting industry. Lorem Ipsum has been the industry's standard dummy text ever since</p>
    </article>
  </section>

  <aside class="birthdays">
    <div class="abs bday-head">
      <svg width="22" height="22" viewBox="0 0 22 22"><rect x="1" y="3" width="20" height="18" rx="2" fill="none" stroke="#fff" stroke-width="2"/><rect x="5" y="0" width="2" height="5" fill="#fff"/><rect x="15" y="0" width="2" height="5" fill="#fff"/><g fill="#fff"><rect x="5" y="9" width="3" height="3"/><rect x="10" y="9" width="3" height="3"/><rect x="15" y="9" width="3" height="3"/><rect x="5" y="14" width="3" height="3"/><rect x="10" y="14" width="3" height="3"/><rect x="15" y="14" width="3" height="3"/></g></svg>
      <div><h3>Author Birthdays</h3><small>FEB 6, 2014</small></div>
    </div>
    <div class="abs bday-item" style="top:454px"><div class="pic" role="img" aria-label="Author portrait"></div><div class="nm">John Smith</div><div class="yr">1890-1970</div></div>
    <div class="abs dotted" style="top:523px"></div>
    <div class="abs bday-item" style="top:532px"><div class="pic" role="img" aria-label="Author portrait"></div><div class="nm">John Smith</div><div class="yr">1890-1970</div></div>
    <div class="abs dotted" style="top:603px"></div>
    <div class="abs bday-item" style="top:616px"><div class="pic" role="img" aria-label="Author portrait"></div><div class="nm">John Smith</div><div class="yr">1890-1970</div></div>
    <div class="abs rule" style="top:686px"></div>
    <div class="abs view-all">VIEW ALL →</div>
    <div class="abs rule" style="top:729px"></div>
  </aside>

  <section class="featured">
    <h2 class="abs featured-bar">FEATURED WEBSITES</h2>
    <div class="abs featured-img" role="img" aria-label="Keyboard with a blue web traffic key"></div>
    <div class="abs featured-title">TRADE CHATTER</div>
    <p class="abs featured-text">Lorem ipsum dolor sit amet, consectetur adipiscing elit, sed do eiusmod tempor incididunt ut labore et dolore magna aliqua. Ut enim ad minim veniam, quis nostrud exercitation ullamco laboris nisi ut aliquip ex ea commodo consequat.</p>
  </section>

  <aside class="seo">
    <h2 class="abs seo-title">SEO TRAINING &amp;<br>INTERNET MARKETING</h2>
    <div class="abs chart" role="img" aria-label="Promotional graphic: survey results on how blogs support SEO"></div>
  </aside>

  <footer>
    <div class="abs footer"></div>
    <div class="abs get-connected">Get Connected</div>
    <div class="abs social"><span style="background:#1c5590"></span><span style="background:#1b9de2"></span><span style="background:#f39317"></span><span style="background:#cfcfcf"></span></div>
    <div class="abs vline" style="left:248px"></div>
    <div class="abs foot-links"><span>Dashboard</span><span>Chirpline Followers</span><span>Submit Chirp</span><span>Activity Summary</span><br><span>Buy Credits</span><span>Settings</span><span>Affiliates</span></div>
    <div class="abs vline" style="left:668px"></div>
    <div class="abs foot-logo"><span class="dot"></span>PlumEcho</div>
    <div class="abs copy">Copyright © 2014 All Rights Reserved | Privacy Policy</div>
  </footer>

</div>
</body>
</html>
```